BrovaLT BIZ Card, email signature & Stationary

Professional business cards, email signatures and ms word letterhead

Target Market(s)

business owners

Industry/Entity Type

cloud hosting

Contact Information for Business Card

name title office phone number , direct line, fax email address web site

Font styles to use
Other font styles liked:
• something that compliments font in logo

```html
<!DOCTYPE html>
<html lang="en">
<head>
<meta charset="utf-8">
<title>BrovaLT Business Card</title>
<link href="https://fonts.googleapis.com/css2?family=Open+Sans:wght@300;400;600;700&family=Montserrat:wght@600&display=swap" rel="stylesheet">
<style>
  :root {
    --backdrop: #e6e6e6;
    --paper: #f4f4f4;
    --ink: #121212;
    --ink-soft: #1d1d1d;
    --brand-red: #d3262b;
    --muted: #c9c9c9;
    --divider: #d7d7d7;
  }
  * { box-sizing: border-box; margin: 0; padding: 0; }
  html, body { width: 1200px; height: 801px; overflow: hidden; }
  body {
    background: radial-gradient(ellipse at 50% 35%, #f2f2f2 0%, var(--backdrop) 60%, #cfcfcf 100%);
    font-family: "Open Sans", sans-serif;
    position: relative;
  }
  .card {
    position: absolute;
    width: 520px;
    height: 298px;
    top: 252px;
    overflow: hidden;
    box-shadow: 0 10px 24px rgba(0,0,0,.22), 0 2px 4px rgba(0,0,0,.15);
  }
  .card--front { left: 50px; background: var(--paper); }
  .card--back  { left: 630px; background: var(--ink); }

  .front-shapes { position: absolute; inset: 0; }

  .wordmark {
    position: absolute;
    font-family: "Open Sans", sans-serif;
    font-weight: 300;
    color: var(--brand-red);
    letter-spacing: -1px;
    line-height: 1;
  }
  .card--front .wordmark { left: 170px; top: 36px; font-size: 78px; }
  .card--back .wordmark { left: 0; right: 0; top: 96px; text-align: center; font-size: 92px; }

  .identity {
    position: absolute;
    left: 300px;
    top: 196px;
    width: 210px;
  }
  .identity__name {
    font-family: "Montserrat", sans-serif;
    font-weight: 600;
    font-size: 17px;
    color: var(--brand-red);
    letter-spacing: .5px;
  }
  .identity__title {
    font-size: 13px;
    color: #eeeeee;
    margin-top: 2px;
  }

  .address {
    position: absolute;
    left: 22px;
    top: 128px;
    font-size: 11px;
    line-height: 1.45;
    color: var(--muted);
  }
  .contacts {
    position: absolute;
    left: 22px;
    top: 196px;
    list-style: none;
    font-size: 11.5px;
    color: #f7f7f7;
  }
  .contacts li { display: flex; align-items: center; gap: 7px; height: 20px; }
  .contacts svg { width: 13px; height: 13px; flex: none; }

  .web {
    position: absolute;
    left: 0; right: 0;
    top: 222px;
    text-align: center;
    font-size: 13px;
    color: #bdbdbd;
    letter-spacing: .3px;
  }
</style>
</head>
<body>

<section class="card card--front" aria-label="Business card front">
  <svg class="front-shapes" viewBox="0 0 520 298" width="520" height="298" aria-hidden="true">
    <polygon points="0,108 175,108 212,298 0,298" fill="var(--divider)"/>
    <polygon points="0,118 170,118 205,298 0,298" fill="var(--ink)"/>
    <polygon points="0,180 200,180 222,205 250,298 0,298" fill="var(--brand-red)"/>
    <polygon points="232,168 520,168 520,298 258,298" fill="var(--ink)"/>
  </svg>

  <div class="wordmark">BrovaLT</div>

  <div class="identity">
    <p class="identity__name">DANA WHITCOMBE</p>
    <p class="identity__title">Managing Director</p>
  </div>

  <p class="address">48 Harbor Lane,<br>Suite 210, Tulsa, OK 74103</p>

  <ul class="contacts">
    <li>
      <svg viewBox="0 0 16 16"><circle cx="8" cy="8" r="8" fill="var(--ink)"/><path d="M5 4.5l1.5-.5 1 2-1 .8a5 5 0 0 0 2.7 2.7l.8-1 2 1-.5 1.5C8.5 11.5 4.5 7.5 5 4.5z" fill="#fff"/></svg>
      (888) 555-0142
    </li>
    <li>
      <svg viewBox="0 0 16 16"><circle cx="8" cy="8" r="8" fill="var(--ink)"/><rect x="5.5" y="3.5" width="5" height="9" rx="1" fill="none" stroke="#fff" stroke-width="1.2"/></svg>
      (000) 000-0000
    </li>
    <li>
      <svg viewBox="0 0 16 16"><circle cx="8" cy="8" r="8" fill="var(--ink)"/><rect x="4" y="7" width="8" height="5" fill="#fff"/><rect x="5.5" y="4" width="5" height="3" fill="none" stroke="#fff" stroke-width="1"/></svg>
      (000) 000-0000
    </li>
    <li>
      <svg viewBox="0 0 16 16"><circle cx="8" cy="8" r="8" fill="var(--ink)"/><rect x="4" y="5" width="8" height="6" fill="none" stroke="#fff" stroke-width="1"/><path d="M4 5l4 3.5L12 5" fill="none" stroke="#fff" stroke-width="1"/></svg>
      info@brovalt.com
    </li>
  </ul>
</section>

<section class="card card--back" aria-label="Business card back">
  <div class="wordmark">BrovaLT</div>
  <p class="web">www.brovalt.com</p>
</section>

</body>
</html>
```